Brindle and Fern LLC | Land Clearing, Landscaping & Dump Trailer Services

Project Description: Brindle and Fern LLC Website Design
The website will be published using squarespace
Objective:
Design a visually compelling and conversion-driven website for Brindle and Fern LLC, a land solutions business based in Pickens County, Georgia. The site will highlight the company’s professionalism, locally rooted service, and commitment to quality in land clearing, grading, and dump trailer services.
Pages & Features to Include:
1. Landing Page (Homepage)
- Clear tagline: Sculpting Land with Precision and Power
- Call-to-Action (CTA) buttons: “Get a Free Quote” and “View Services”
- Service highlights with icons or photos (e.g., grading, mulching, hauling)
- Customer testimonials
- Embedded contact form
- Google Maps integration showing service area
2. Services + Pricing Page
- Organized list of services under 3 categories:
- **Land Clearing & Grading**
- Forestry Mulching
- Gravel Driveway Repair
- Minimum Job Fee:
- Dump Trailer Services
- Trailer Rental (Daily):
- Junk Removal (Full Load)
- Material Delivery: $ + mileage
- Specialty Jobs
- Stump removal, light demolition
- Each service section includes short descriptions and photos
- Optional quote form at the bottom with “Request a Quote” CTA
Design Style:
- Clean, professional design using clean tones
- Fonts that balance industrial strength and local charm
- Mobile-optimized with fast loading speeds and easy navigation
- SEO-optimized for terms like *land clearing Pickens County*, *grading services North Georgia*, and *dump trailer rental Jasper GA*, etc...

```html
<!DOCTYPE html>
<html lang="en">
<head>
<meta charset="utf-8">
<title>Brindle and Fern LLC | Land Clearing, Grading &amp; Dump Trailer Services</title>
<link href="https://fonts.googleapis.com/css2?family=Roboto:wght@400;500;700;900&display=swap" rel="stylesheet">
<style>
:root{
  --green:#4a8c2f;
  --green-dark:#3f7a27;
  --green-soft:#eef6e6;
  --ink:#222222;
  --muted:#555555;
  --white:#ffffff;
  --line:#dcdcdc;
  --star:#f5b400;
}
*{margin:0;padding:0;box-sizing:border-box}
html,body{width:1200px;height:2600px;overflow:hidden}
body{position:relative;font-family:'Roboto',sans-serif;color:var(--ink);background:var(--white)}
.abs{position:absolute}
a{color:inherit;text-decoration:none}

/* header */
.site-header{left:0;top:0;width:1200px;height:62px;background:var(--white);z-index:5}
.brand{left:215px;top:0;width:150px;height:125px;background:var(--white);border-radius:0 0 22px 22px;z-index:6;display:flex;align-items:center;justify-content:center;gap:8px;padding:0 12px}
.brand-mark{width:12px;height:12px;background:var(--green);flex:none}
.brand-name{font-weight:700;font-size:15px;line-height:1.2;color:var(--ink)}
.nav{top:0;left:576px;height:62px;display:flex;align-items:center;font-size:10px;z-index:6}
.nav a{margin-right:34px}
.nav a.active{color:var(--green)}
.btn{display:inline-flex;align-items:center;justify-content:center;font-size:10px;font-weight:500;border-radius:2px}
.btn-solid{background:var(--green);color:var(--white)}
.btn-light{background:var(--white);color:var(--ink)}
.btn-outline{border:1.5px solid var(--white);color:var(--white);border-radius:3px}
.nav-cta{left:884px;top:17px;width:100px;height:28px;z-index:6}

/* hero */
.hero-photo{left:0;top:62px;width:1200px;height:620px;background:linear-gradient(100deg,#5b6a3a 0%,#6f7a46 35%,#8a8d5b 60%,#9aa29a 80%,#6c7660 100%)}
.hero-tags{left:215px;top:250px;color:var(--white);font-weight:700;font-size:12.5px;letter-spacing:.3px}
.hero-title{left:214px;top:274px;color:var(--white);font-weight:700;font-size:47px;line-height:56px}
.hero-title em{font-style:normal;color:var(--green)}
.hero-quote{left:215px;top:424px;width:100px;height:27px}
.hero-services{left:325px;top:424px;width:88px;height:27px}

/* intro band */
.intro-band{left:0;top:600px;width:1200px;height:400px}
.intro-title{left:0;top:733px;width:1200px;text-align:center;color:var(--white);font-weight:700;font-size:28px}
.intro-sub{left:0;top:780px;width:1200px;text-align:center;color:var(--white);font-size:17.5px}
.intro-cta{left:550px;top:823px;width:100px;height:27px}

/* service cards */
.services{left:215px;top:913px;display:flex;gap:19px}
.service-card{width:178px;height:172px;background:var(--white);box-shadow:0 2px 8px rgba(0,0,0,.08);text-align:center;padding-top:26px}
.service-icon{display:block;margin:0 auto}
.service-card h3{font-size:11.5px;font-weight:500;margin-top:14px}
.service-card p{font-size:8.5px;color:var(--muted);line-height:13.5px;margin:12px 18px 0;height:28px}
.service-card .more{display:block;font-size:9px;color:var(--green);margin-top:14px}

/* about */
.about-title{left:215px;top:1164px;font-size:28px;font-weight:700}
.about-copy{left:215px;top:1219px;width:375px;font-size:8.7px;line-height:15px;color:var(--muted)}
.about-copy p{margin-bottom:15px}
.about-cta{left:215px;top:1372px;width:100px;height:27px}
.photo-main{left:672px;top:1148px;width:312px;height:237px;border-radius:4px;background:linear-gradient(135deg,#7a8a55,#a89a6a 55,#c9a23a 80%,#6b7d45)}
.photo-small{left:632px;top:1302px;width:154px;height:122px;border-radius:6px;border:4px solid var(--white);background:linear-gradient(160deg,#b8bcc0,#6a7ea6 55%,#8a8a86)}

/* testimonials */
.reviews{left:0;top:1485px;width:1200px;height:405px;background:var(--green-soft)}
.reviews-title{left:0;top:1528px;width:1200px;text-align:center;font-size:27px;font-weight:700}
.reviews-title em{font-style:normal;color:var(--green)}
.review-list{left:215px;top:1600px;display:flex;gap:18px}
.review{width:244px}
.review-card{position:relative;background:var(--white);height:151px;padding:26px 20px 0}
.review-card::after{content:"";position:absolute;left:22px;bottom:-8px;border-left:7px solid transparent;border-right:7px solid transparent;border-top:8px solid var(--white)}
.review-card p{font-size:9.3px;line-height:16.2px;color:var(--muted)}
.stars{color:var(--star);font-size:11px;letter-spacing:1px;margin-top:12px}
.reviewer{display:flex;align-items:center;margin:13px 0 0 25px}
.avatar{width:38px;height:38px;border-radius:50%;background:#b3b3b3}
.reviewer-info{margin-left:9px}
.reviewer-info small{display:block;font-size:9px;color:var(--green)}
.reviewer-info strong{display:block;font-size:11px;font-weight:500;margin-top:4px}
.dots{left:584px;top:1831px;display:flex;gap:6px}
.dots span{width:7px;height:7px;border-radius:50%;background:#8fbe73}
.dots span.on{background:var(--green)}

/* contact */
.contact-title{left:215px;top:1945px;font-size:27px;font-weight:700;line-height:34px}
.contact-title em{font-style:normal;color:var(--green)}
.contact-copy{left:215px;top:2034px;width:375px;font-size:8.7px;line-height:15px;color:var(--muted)}
.field-label{font-size:8.7px;color:var(--ink)}
.input{border:1px solid var(--line);background:var(--white);border-radius:2px}
.send{left:215px;top:2288px;width:100px;height:27px}
.info-box{top:1987px;height:50px;background:var(--green-soft);display:flex;align-items:center;justify-content:center;gap:9px;font-size:8.7px}
.map{left:634px;top:2055px;width:351px;height:263px;background:linear-gradient(160deg,#d7f0e6,#cdeede 50%,#e1f3e8)}

/* footer */
.footer{left:0;top:2380px;width:1200px;height:220px}
.socials{left:530px;top:2512px;display:flex;gap:11px}
.socials span{width:19px;height:19px;border-radius:50%;border:1.5px solid var(--white)}
.copyright{left:0;top:2556px;width:1200px;text-align:center;color:var(--white);font-size:8.5px;font-weight:500}
</style>
</head>
<body>

<header>
  <div class="abs site-header"></div>
  <a class="abs brand" href="#"><span class="brand-mark"></span><span class="brand-name">Brindle and Fern LLC</span></a>
  <nav class="abs nav">
    <a class="active" href="#">Home</a><a href="#">About</a><a href="#">Services &amp; Pricing</a><a href="#">Gallery</a>
  </nav>
  <a class="abs btn btn-solid nav-cta" href="#">Contact Us Now!</a>
</header>

<section>
  <div class="abs hero-photo" role="img" aria-label="Photo of an excavator clearing trees in a forest"></div>
  <div class="abs hero-tags">LAND CLEARING &nbsp;|&nbsp; GRADING &nbsp;|&nbsp; DUMP TRAILER SERVICES</div>
  <h1 class="abs hero-title">Sculpting Land with<br><em>Precision</em> &amp; Power</h1>
  <a class="abs btn btn-solid hero-quote" href="#">Get a Free Quote</a>
  <a class="abs btn btn-light hero-services" href="#">View Services</a>
</section>

<section>
  <svg class="abs intro-band" viewBox="0 0 1200 400" preserveAspectRatio="none" aria-hidden="true">
    <path d="M0 0 L80 25 L330 70 L640 45 L900 28 L1200 15 L1200 400 L0 400 Z" fill="#4a8c2f"/>
  </svg>
  <h2 class="abs intro-title">Brindle and Fern LLC</h2>
  <p class="abs intro-sub">Land solutions business based in Pickens County, Georgia.</p>
  <a class="abs btn btn-outline intro-cta" href="#">Get a Free Quote</a>

  <div class="abs services">
    <article class="service-card">
      <svg class="service-icon" width="32" height="28" viewBox="0 0 32 28" aria-hidden="true"><rect x="4" y="10" width="24" height="10" rx="2" fill="none" stroke="#4a8c2f" stroke-width="2"/><circle cx="10" cy="23" r="3" fill="#4a8c2f"/><circle cx="22" cy="23" r="3" fill="#4a8c2f"/></svg>
      <h3>Land Clearing</h3>
      <p>Clear trees, brush, and debris fast, ready your land for any project.</p>
      <a class="more" href="#">View Details</a>
    </article>
    <article class="service-card">
      <svg class="service-icon" width="32" height="28" viewBox="0 0 32 28" aria-hidden="true"><path d="M3 24 H29" stroke="#4a8c2f" stroke-width="2"/><path d="M8 22 V8 M16 22 V4 M24 22 V10" stroke="#4a8c2f" stroke-width="2"/></svg>
      <h3>Grading</h3>
      <p>Smooth, level surfaces for driveways, drainage, or site prep.</p>
      <a class="more" href="#">View Details</a>
    </article>
    <article class="service-card">
      <svg class="service-icon" width="32" height="28" viewBox="0 0 32 28" aria-hidden="true"><path d="M10 24 L16 6 L22 24 Z" fill="#4a8c2f"/><path d="M3 25 H29" stroke="#4a8c2f" stroke-width="2"/></svg>
      <h3>Forestry Mulching</h3>
      <p>Mulch overgrowth on-site, no burning, no hauling.</p>
      <a class="more" href="#">View Details</a>
    </article>
    <article class="service-card">
      <svg class="service-icon" width="32" height="28" viewBox="0 0 32 28" aria-hidden="true"><rect x="3" y="8" width="18" height="11" fill="none" stroke="#4a8c2f" stroke-width="2"/><rect x="21" y="12" width="8" height="7" fill="none" stroke="#4a8c2f" stroke-width="2"/><circle cx="9" cy="22" r="3" fill="#4a8c2f"/><circle cx="24" cy="22" r="3" fill="#4a8c2f"/></svg>
      <h3>Dump Trailer Services</h3>
      <p>Rent, load, and go, trailers for junk, gravel, or delivery.</p>
      <a class="more" href="#">View Details</a>
    </article>
  </div>
</section>

<section>
  <h2 class="abs about-title">Brindle and Fern LLC</h2>
  <div class="abs about-copy">
    <p>We take pride in shaping the land with precision, offering expert land clearing, grading, and dump trailer services across Pickens County and North Georgia.</p>
    <p>Our dedicated crew brings skill, professionalism, and a commitment to quality on every job, big or small.Rooted in the community we serve, we hold ourselves to high standards and a strong work ethic.</p>
    <p>Let’s talk about how we can bring your next land project to life.</p>
  </div>
  <a class="abs btn btn-solid about-cta" href="#">Contact Us Now!</a>
  <div class="abs photo-main" role="img" aria-label="Photo of a yellow excavator clearing pine forest"></div>
  <div class="abs photo-small" role="img" aria-label="Photo of a blue dump trailer at a gravel site"></div>
</section>

<section>
  <div class="abs reviews"></div>
  <h2 class="abs reviews-title">What They <em>Say</em> About Us?</h2>
  <div class="abs review-list">
    <div class="review">
      <div class="review-card"><p>“It is a long established fact that a reader will be distracted by the readable content of a page when looking at its layout. The point of using Lorem Ipsum is that it has a more or less normal distribution of letters.”</p><div class="stars">★★★★★</div></div>
      <div class="reviewer"><span class="avatar"></span><div class="reviewer-info"><small>Georgia</small><strong>Dale Whitaker</strong></div></div>
    </div>
    <div class="review">
      <div class="review-card"><p>“It is a long established fact that a reader will be distracted by the readable content of a page when looking at its layout. The point of using Lorem Ipsum is that it has a more or less normal distribution of letters.”</p><div class="stars">★★★★★</div></div>
      <div class="reviewer"><span class="avatar"></span><div class="reviewer-info"><small>Georgia</small><strong>Dale Whitaker</strong></div></div>
    </div>
    <div class="review">
      <div class="review-card"><p>“It is a long established fact that a reader will be distracted by the readable content of a page when looking at its layout. The point of using Lorem Ipsum is that it has a more or less normal distribution of letters.”</p><div class="stars">★★★★★</div></div>
      <div class="reviewer"><span class="avatar"></span><div class="reviewer-info"><small>Georgia</small><strong>Dale Whitaker</strong></div></div>
    </div>
  </div>
  <div class="abs dots"><span></span><span class="on"></span><span></span></div>
</section>

<section>
  <h2 class="abs contact-title">Need Help?<br>Feel Free To <em>Contact Us</em> Now!</h2>
  <p class="abs contact-copy">We take pride in shaping the land with precision, offering expert land clearing, grading, and dump trailer services across Pickens County and North Georgia.</p>
  <label class="abs field-label" style="left:215px;top:2096px">Full Name*</label>
  <div class="abs input" style="left:215px;top:2114px;width:178px;height:27px"></div>
  <label class="abs field-label" style="left:412px;top:2096px">E-mail Address*</label>
  <div class="abs input" style="left:412px;top:2114px;width:178px;height:27px"></div>
  <label class="abs field-label" style="left:215px;top:2165px">Your Message*</label>
  <div class="abs input" style="left:216px;top:2183px;width:375px;height:87px"></div>
  <a class="abs btn btn-solid send" href="#">Send Message</a>

  <div class="abs info-box" style="left:634px;width:166px">
    <svg width="15" height="11" viewBox="0 0 15 11" aria-hidden="true"><rect width="15" height="11" rx="1" fill="#4a8c2f"/><path d="M1 1 L7.5 6 L14 1" stroke="#eef6e6" stroke-width="1.3" fill="none"/></svg>
    <span>info@brindlefern.com</span>
  </div>
  <div class="abs info-box" style="left:818px;width:166px">
    <svg width="14" height="14" viewBox="0 0 24 24" aria-hidden="true"><path d="M6.6 10.8a15 15 0 0 0 6.6 6.6l2.2-2.2c.3-.3.7-.4 1-.2 1.1.4 2.3.6 3.6.6.6 0 1 .4 1 1V20c0 .6-.4 1-1 1A17 17 0 0 1 3 4c0-.6.4-1 1-1h3.5c.6 0 1 .4 1 1 0 1.3.2 2.5.6 3.6.1.3 0 .7-.2 1z" fill="#4a8c2f"/></svg>
    <span>+1 (555) - 014 - 2290</span>
  </div>
  <div class="abs map" role="img" aria-label="Map of the Pickens County service area"></div>
</section>

<footer>
  <svg class="abs footer" viewBox="0 0 1200 220" preserveAspectRatio="none" role="img" aria-label="Green tinted photo of equipment on a work site">
    <path d="M0 0 L360 60 L980 8 L1200 30 L1200 220 L0 220 Z" fill="#c9dcbc"/>
    <path d="M0 30 L350 70 L1000 18 L1200 40 L1200 220 L0 220 Z" fill="#5a9a3c"/>
    <rect x="0" y="110" width="1200" height="110" fill="#4f8e33" opacity=".6"/>
  </svg>
  <div class="abs socials"><span></span><span></span><span></span><span></span><span></span></div>
  <p class="abs copyright">Copyright © 2025 Brindle and Fern LLC | All Rights Reserved.</p>
</footer>

</body>
</html>
```